Flyer for Children Therapy Center

We need a flyer with front and back with the following services:

Services:
- Entre outros!

Products:

Target Market(s)

Parents of children with special needs

Colors

Designer to choose colors to be used in the design.

Requirements
Must have
• The flyer must have:
• - Our logo
• - Company Name: Raiz Doce Luz
• - center description: Centro de Terapias Especializadas para crianças e jovens.
• - Slogan: Semeamos amor, colhemos sorrisos, distribuímos vitórias!
• - Site: www.ramolu.pt
• - Facebook: www.facebook.com/raizdoceluz
• - Cellular phone: +351 915 487 062
• - Land Line: +351 218 640 275
• - E-mail: geral@ramolu.pt
• - Address: R. Fernando Queirós Pimentel 3B, 2610-187 - Póvoa de Santa Iria, Portugal
Nice to have
• Logo colors
Should not have
• Dark colors.

```html
<!DOCTYPE html>
<html lang="pt">
<head>
<meta charset="utf-8">
<title>Raiz Doce Luz — Flyer frente e verso</title>
<link rel="stylesheet" href="https://fonts.googleapis.com/css2?family=Arvo:ital,wght@1,700&family=Didact+Gothic&family=Josefin+Sans:wght@700&display=swap">
<style>
  :root{
    --purple:#7b2d6e;
    --teal:#1aa89a;
    --red:#e8433c;
    --yellow:#f6c200;
    --grey:#8c8c8c;
    --ink:#555555;
    --paper:#ffffff;
    --backdrop:#ebe8e4;
  }
  html,body{margin:0;padding:0;overflow:hidden;}
  body{width:1200px;height:808px;background:var(--backdrop);position:relative;}
  .flyer{position:absolute;top:60px;width:486px;height:688px;background:var(--paper);box-shadow:0 2px 8px rgba(0,0,0,.18);overflow:hidden;}
  .flyer--front{left:66px;}
  .flyer--back{left:665px;}
  .flyer svg{display:block;width:486px;height:688px;}
  .title{font-family:"Josefin Sans",sans-serif;font-weight:700;fill:var(--purple);}
  .slogan{font-family:"Arvo",serif;font-style:italic;font-weight:700;fill:var(--grey);}
  .heading{font-family:"Didact Gothic",sans-serif;fill:var(--teal);}
  .item{font-family:"Didact Gothic",sans-serif;fill:var(--ink);}
  .bullet{fill:none;stroke:var(--ink);stroke-width:1;}
  .brand-name{font-family:"Didact Gothic",sans-serif;fill:var(--red);}
  .brand-site{font-family:"Didact Gothic",sans-serif;fill:var(--purple);}
  .badge-label{font-family:"Didact Gothic",sans-serif;fill:#fff;}
  .contact{font-family:"Didact Gothic",sans-serif;fill:#fff;}
  .phone{font-family:"Josefin Sans",sans-serif;font-weight:700;fill:#fff;}
  .photo-ring{stroke:var(--yellow);stroke-width:4;}
  .social-mark{fill:var(--yellow);}
</style>
</head>
<body>

<!-- Front -->
<section class="flyer flyer--front">
<svg viewBox="0 0 584 827" xmlns="http://www.w3.org/2000/svg">
  <defs>
    <linearGradient id="heroFront" x1="0" y1="0" x2="1" y2="1">
      <stop offset="0" stop-color="#d9c7a8"/>
      <stop offset=".5" stop-color="#e9b86a"/>
      <stop offset="1" stop-color="#8fb0d6"/>
    </linearGradient>
    <linearGradient id="rule" x1="0" x2="1">
      <stop offset="0" stop-color="#f6c200" stop-opacity="0"/>
      <stop offset=".5" stop-color="#f6c200"/>
      <stop offset="1" stop-color="#f6c200" stop-opacity="0"/>
    </linearGradient>
    <clipPath id="roundFront" clipPathUnits="objectBoundingBox"><circle cx=".5" cy=".5" r=".5"/></clipPath>
  </defs>

  <g role="img" aria-label="Fotografia: criança em sessão de terapia ocupacional com terapeuta numa sala colorida">
    <rect x="0" y="0" width="584" height="340" fill="url(#heroFront)"/>
  </g>

  <!-- brand circle -->
  <circle cx="495" cy="150" r="178" fill="var(--paper)"/>
  <path d="M360,40 A178,178 0 0 0 400,290" fill="none" stroke="var(--teal)" stroke-width="5"/>
  <circle cx="485" cy="160" r="44" fill="var(--teal)"/>
  <text class="brand-name" x="495" y="245" font-size="17" text-anchor="middle">Raiz Doce Luz</text>
  <text class="brand-site" x="495" y="265" font-size="13" text-anchor="middle">www.ramolu.pt</text>

  <!-- purple wave -->
  <path d="M0,268 C180,330 420,338 584,312" fill="none" stroke="#cfcfcf" stroke-width="2"/>
  <path d="M0,275 C180,335 420,342 584,318 L584,334 C420,356 180,350 0,318 Z" fill="var(--purple)"/>
  <path d="M0,318 C180,350 420,356 584,334 L584,827 L0,827 Z" fill="var(--paper)"/>

  <!-- headline -->
  <text class="title" x="391" y="366" font-size="19" text-anchor="middle">Centro de Terapias Especializadas</text>
  <text class="title" x="391" y="391" font-size="19" text-anchor="middle">para crianças e jovens</text>
  <rect x="225" y="412" width="335" height="2" fill="url(#rule)"/>
  <text class="slogan" x="391" y="434" font-size="13" text-anchor="middle">Semeamos amor, colhemos sorrisos,</text>
  <text class="slogan" x="391" y="452" font-size="13" text-anchor="middle">distribuímos vitórias!</text>

  <!-- services -->
  <text class="heading" x="240" y="498" font-size="20">SERVIÇOS</text>
  <g class="service-list" font-size="17.5">
    <circle class="bullet" cx="250" cy="520" r="5"/><text class="item" x="267" y="526">Fisioterapia</text>
    <circle class="bullet" cx="250" cy="547" r="5"/><text class="item" x="267" y="553">Terapia Ocupacional</text>
    <circle class="bullet" cx="250" cy="575" r="5"/><text class="item" x="267" y="581">Terapia da Fala</text>
    <circle class="bullet" cx="250" cy="602" r="5"/><text class="item" x="267" y="608">Musicoterapia</text>
    <circle class="bullet" cx="250" cy="630" r="5"/><text class="item" x="267" y="636">Estimulação Elétrica Neurofuncional</text>
    <circle class="bullet" cx="250" cy="657" r="5"/><text class="item" x="267" y="663">Entre outros!</text>
  </g>

  <!-- footer bands -->
  <path d="M0,712 C160,735 350,662 584,662 L584,827 L0,827 Z" fill="var(--yellow)"/>
  <path d="M0,718 C170,742 360,672 584,676 L584,827 L0,827 Z" fill="var(--paper)"/>
  <path d="M0,726 C180,748 370,688 584,700 L584,827 L0,827 Z" fill="var(--red)"/>

  <!-- service photos -->
  <g clip-path="url(#roundFront)" role="img" aria-label="Fotografia: criança em exercício de terapia ocupacional sobre bola">
    <circle cx="117" cy="304" r="80" fill="#b9a6c7"/>
    <rect x="37" y="356" width="160" height="30" fill="var(--purple)"/>
  </g>
  <circle class="photo-ring" cx="117" cy="304" r="80" fill="none"/>
  <text class="badge-label" x="117" y="374" font-size="11" text-anchor="middle">Ocupacional</text>

  <g clip-path="url(#roundFront)" role="img" aria-label="Fotografia: criança em sessão de terapia da fala com cartões">
    <circle cx="117" cy="484" r="80" fill="#e6cfa4"/>
    <rect x="37" y="536" width="160" height="30" fill="var(--purple)"/>
  </g>
  <circle class="photo-ring" cx="117" cy="484" r="80" fill="none"/>
  <text class="badge-label" x="117" y="554" font-size="11" text-anchor="middle">Terapia da Fala</text>

  <g clip-path="url(#roundFront)" role="img" aria-label="Fotografia: criança sorridente de braços abertos durante estimulação elétrica">
    <circle cx="117" cy="664" r="80" fill="#a9c8c2"/>
    <rect x="37" y="706" width="160" height="40" fill="var(--purple)"/>
  </g>
  <circle class="photo-ring" cx="117" cy="664" r="80" fill="none"/>
  <text class="badge-label" x="117" y="719" font-size="9.5" text-anchor="middle">Elétrica</text>
  <text class="badge-label" x="117" y="729" font-size="9.5" text-anchor="middle">Neurofuncional</text>

  <!-- contacts -->
  <path d="M392,752 l5,-3 l4,7 l-3,2 c1,3 3,6 6,8 l2,-3 l7,4 l-3,5 c-9,0 -18,-10 -18,-20 z" fill="var(--yellow)"/>
  <text class="phone" x="562" y="762" font-size="17.5" text-anchor="end">+351 915 487 062</text>
  <text class="phone" x="562" y="784" font-size="17.5" text-anchor="end">+351 218 640 275</text>
  <rect class="social-mark" x="24" y="773" width="17" height="17" rx="3"/>
  <text class="contact" x="52" y="787" font-size="13">/raizdoceluz</text>
  <text class="contact" x="22" y="811" font-size="11.2">geral@ramolu.pt  |  R. Fernando Queirós Pimentel 3B, 2610-187 - Póvoa de Santa Iria, Portugal</text>
</svg>
</section>

<!-- Back -->
<section class="flyer flyer--back">
<svg viewBox="0 0 584 827" xmlns="http://www.w3.org/2000/svg">
  <defs>
    <linearGradient id="heroBack" x1="0" y1="0" x2="1" y2="1">
      <stop offset="0" stop-color="#e4e2dc"/>
      <stop offset=".55" stop-color="#c99a7e"/>
      <stop offset="1" stop-color="#7a4e36"/>
    </linearGradient>
    <linearGradient id="ruleBack" x1="0" x2="1">
      <stop offset="0" stop-color="#f6c200" stop-opacity="0"/>
      <stop offset=".5" stop-color="#f6c200"/>
      <stop offset="1" stop-color="#f6c200" stop-opacity="0"/>
    </linearGradient>
    <clipPath id="roundBack" clipPathUnits="objectBoundingBox"><circle cx=".5" cy=".5" r=".5"/></clipPath>
  </defs>

  <g role="img" aria-label="Fotografia: terapeuta e criança a rir enquanto tocam guitarra em musicoterapia">
    <rect x="0" y="0" width="584" height="350" fill="url(#heroBack)"/>
  </g>

  <path d="M0,266 C200,296 400,336 584,312" fill="none" stroke="#cfcfcf" stroke-width="2"/>
  <path d="M0,272 C200,302 400,342 584,318 L584,352 C400,362 200,350 0,338 Z" fill="var(--purple)"/>
  <path d="M0,338 C200,350 400,362 584,352 L584,827 L0,827 Z" fill="var(--paper)"/>

  <text class="title" x="292" y="382" font-size="18" text-anchor="middle">Centro de Terapias Especializadas para crianças e jovens</text>
  <rect x="30" y="403" width="524" height="2" fill="url(#ruleBack)"/>
  <text class="slogan" x="292" y="422" font-size="13" text-anchor="middle">Semeamos amor, colhemos sorrisos, distribuímos vitórias!</text>

  <!-- products -->
  <text class="heading" x="275" y="468" font-size="19">PRODUCTS</text>
  <circle cx="517" cy="490" r="24" fill="#eef3e6" stroke="#5a8a3a" stroke-width="2"/>
  <g font-size="16.5">
    <circle class="bullet" cx="282" cy="492" r="5"/><text class="item" x="299" y="498">Fitoterapia Tradicional</text>
    <text class="item" x="299" y="522">Chinesa</text>
    <circle class="bullet" cx="282" cy="540" r="5"/><text class="item" x="299" y="546">Ortóteses dinâmicas funcionais</text>
    <circle class="bullet" cx="282" cy="564" r="5"/><text class="item" x="299" y="570">Fato de compressão dinâmica</text>
    <text class="item" x="299" y="594">sob medida</text>
    <circle class="bullet" cx="282" cy="612" r="5"/><text class="item" x="299" y="618">Assento pélvico moldado com</text>
    <text class="item" x="299" y="642">técnica exclusiva</text>
  </g>

  <!-- footer bands -->
  <path d="M0,712 C160,735 350,662 584,662 L584,827 L0,827 Z" fill="var(--yellow)"/>
  <path d="M0,718 C170,742 360,672 584,676 L584,827 L0,827 Z" fill="var(--paper)"/>
  <path d="M0,726 C180,748 370,688 584,700 L584,827 L0,827 Z" fill="var(--red)"/>

  <!-- before / after photos -->
  <g clip-path="url(#roundBack)" role="img" aria-label="Fotografia: pés antes do tratamento">
    <circle cx="71" cy="487" r="48" fill="#d8b8a3"/><rect x="23" y="517" width="96" height="20" fill="var(--purple)"/>
  </g>
  <circle class="photo-ring" cx="71" cy="487" r="48" fill="none"/>
  <text class="badge-label" x="71" y="529" font-size="9.5" text-anchor="middle">Before</text>

  <g clip-path="url(#roundBack)" role="img" aria-label="Fotografia: pés depois do tratamento">
    <circle cx="180" cy="487" r="48" fill="#e3a98a"/><rect x="132" y="517" width="96" height="20" fill="var(--purple)"/>
  </g>
  <circle class="photo-ring" cx="180" cy="487" r="48" fill="none"/>
  <text class="badge-label" x="180" y="529" font-size="9.5" text-anchor="middle">After</text>

  <g clip-path="url(#roundBack)" role="img" aria-label="Fotografia: postura das costas antes do tratamento">
    <circle cx="71" cy="597" r="48" fill="#d9b49a"/><rect x="23" y="627" width="96" height="20" fill="var(--purple)"/>
  </g>
  <circle class="photo-ring" cx="71" cy="597" r="48" fill="none"/>
  <text class="badge-label" x="71" y="639" font-size="9.5" text-anchor="middle">Before</text>

  <g clip-path="url(#roundBack)" role="img" aria-label="Fotografia: postura com fato de compressão depois do tratamento">
    <circle cx="180" cy="597" r="48" fill="#5f7fb0"/><rect x="132" y="627" width="96" height="20" fill="var(--purple)"/>
  </g>
  <circle class="photo-ring" cx="180" cy="597" r="48" fill="none"/>
  <text class="badge-label" x="180" y="639" font-size="9.5" text-anchor="middle">After</text>

  <g clip-path="url(#roundBack)" role="img" aria-label="Fotografia: criança sentada antes do assento moldado">
    <circle cx="71" cy="707" r="48" fill="#8a9bb0"/><rect x="23" y="737" width="96" height="20" fill="var(--purple)"/>
  </g>
  <circle class="photo-ring" cx="71" cy="707" r="48" fill="none"/>
  <text class="badge-label" x="71" y="749" font-size="9.5" text-anchor="middle">Before</text>

  <g clip-path="url(#roundBack)" role="img" aria-label="Fotografia: criança sentada no assento moldado depois">
    <circle cx="180" cy="707" r="48" fill="#c9706a"/><rect x="132" y="737" width="96" height="20" fill="var(--purple)"/>
  </g>
  <circle class="photo-ring" cx="180" cy="707" r="48" fill="none"/>
  <text class="badge-label" x="180" y="749" font-size="9.5" text-anchor="middle">After</text>

  <!-- contacts -->
  <path d="M392,752 l5,-3 l4,7 l-3,2 c1,3 3,6 6,8 l2,-3 l7,4 l-3,5 c-9,0 -18,-10 -18,-20 z" fill="var(--yellow)"/>
  <text class="phone" x="562" y="762" font-size="17.5" text-anchor="end">+351 915 487 062</text>
  <text class="phone" x="562" y="784" font-size="17.5" text-anchor="end">+351 218 640 275</text>
  <rect class="social-mark" x="24" y="773" width="17" height="17" rx="3"/>
  <text class="contact" x="52" y="787" font-size="13">/raizdoceluz</text>
  <text class="contact" x="22" y="811" font-size="11.2">geral@ramolu.pt  |  R. Fernando Queirós Pimentel 3B, 2610-187 - Póvoa de Santa Iria, Portugal</text>
</svg>
</section>

</body>
</html>
```